Norvane Builders Business Card

Modern and Professional Business Card for a Med size construction/development company.

See the samples below for the design I like … but I need ideas for incorporating the red company logo while still keeping the clean look of the card samples that are attached.

Logo and tag line on the back … info on the front.

Tagline: Quality Starts from the Ground Up

Target Market(s)

Med-Large General Contractors

Contact Information for Business Card

Norvane Builders Limited
42 Brenton Street
Elk Harbour, NL
B3K 7T2

t: 709-555-0147
f: 709-555-0192
w: www.norvanebuilders-example.com

Font styles to use
Sans Serif

Colors
fbee3e

Requirements
Must have
• I like the black and yellow designs of the attached samples …. but I'm not sure how to incorporate the red Norvane Builders logo into that design??
Nice to have
• Construction safety strips

```html
<!DOCTYPE html>
<html lang="en">
<head>
<meta charset="utf-8">
<title>Norvane Builders Business Card</title>
<link rel="stylesheet" href="https://fonts.googleapis.com/css2?family=Lato:wght@400;700;900&display=swap">
<style>
  :root {
    --safety-yellow: #f0ea44;
    --pill-yellow: #f5ec20;
    --ink: #050808;
    --charcoal: #3a3a3c;
    --brand-red: #e8202b;
    --white: #ffffff;
  }
  * { margin: 0; padding: 0; box-sizing: border-box; }
  html, body { width: 1080px; height: 1200px; overflow: hidden; background: var(--white); }
  body { position: relative; font-family: "Lato", sans-serif; }

  .card { position: absolute; left: 121px; width: 850px; height: 480px; overflow: hidden; }
  .card--front { top: 76px; background: var(--safety-yellow); }
  .card--back { top: 628px; background: var(--charcoal); }

  .safety-strip { position: absolute; left: 0; width: 850px; height: 60px; display: block; }
  .safety-strip--top { top: 0; }
  .safety-strip--bottom { bottom: 0; }

  .brand-mark {
    position: absolute; left: 0; right: 0; top: 190px;
    display: flex; align-items: center; justify-content: center; gap: 18px;
  }
  .brand-mark__square { width: 44px; height: 44px; background: var(--brand-red); }
  .brand-mark__name {
    font-weight: 900; font-size: 48px; color: var(--ink); letter-spacing: 0.5px;
  }
  .tagline {
    position: absolute; left: 0; right: 0; top: 364px; text-align: center;
    font-size: 26px; color: var(--ink);
  }

  .company-name {
    position: absolute; left: 165px; width: 520px; top: 96px; text-align: center;
    font-weight: 700; font-size: 42px; color: var(--safety-yellow); white-space: nowrap;
  }
  .company-rule {
    position: absolute; left: 165px; width: 520px; top: 166px; height: 4px;
    background: var(--safety-yellow);
  }
  .contact-list { list-style: none; }
  .contact-item {
    position: absolute; left: 177px; width: 499px; height: 50px;
    background: var(--pill-yellow); border: 2px solid var(--white);
    border-left: none; border-radius: 25px 0 0 25px;
    display: flex; align-items: center;
  }
  .contact-item--phone { top: 188px; }
  .contact-item--web { top: 262px; }
  .contact-item--address { top: 337px; }
  .contact-item__icon {
    flex: none; width: 52px; height: 52px; margin-left: -1px;
    border-radius: 50%; border: 2px solid var(--white); background: var(--pill-yellow);
    display: flex; align-items: center; justify-content: center;
  }
  .contact-item__icon svg { width: 32px; height: 32px; display: block; }
  .contact-item__text {
    margin-left: 14px; font-size: 23px; color: var(--ink); white-space: nowrap;
  }
  .contact-item--address .contact-item__text { font-size: 20px; }
</style>
</head>
<body>
<svg width="0" height="0" style="position:absolute">
  <defs>
    <pattern id="strip-dark" patternUnits="userSpaceOnUse" width="81" height="60">
      <polygon points="0,60 41,60 76,0 35,0" fill="#050808"/>
    </pattern>
    <pattern id="strip-light" patternUnits="userSpaceOnUse" width="81" height="60" x="20">
      <polygon points="0,60 41,60 76,0 35,0" fill="#f0ea44"/>
    </pattern>
  </defs>
</svg>

<section class="card card--front" aria-label="Card front">
  <svg class="safety-strip safety-strip--top" viewBox="0 0 850 60"><rect width="850" height="60" fill="url(#strip-dark)"/></svg>
  <div class="brand-mark">
    <span class="brand-mark__square"></span>
    <span class="brand-mark__name">Norvane Builders Limited</span>
  </div>
  <p class="tagline">Quality Starts from the Ground Up</p>
  <svg class="safety-strip safety-strip--bottom" viewBox="0 0 850 60"><rect width="850" height="60" fill="url(#strip-dark)"/></svg>
</section>

<section class="card card--back" aria-label="Card back">
  <svg class="safety-strip safety-strip--top" viewBox="0 0 850 60"><rect width="850" height="60" fill="url(#strip-light)"/></svg>
  <h1 class="company-name">Norvane Builders Limited</h1>
  <div class="company-rule"></div>
  <ul class="contact-list">
    <li class="contact-item contact-item--phone">
      <span class="contact-item__icon">
        <svg viewBox="0 0 24 24"><path fill="#050808" d="M6.6 10.8a15.1 15.1 0 0 0 6.6 6.6l2.2-2.2c.3-.3.7-.4 1-.2 1.1.4 2.3.6 3.6.6.6 0 1 .4 1 1V20c0 .6-.4 1-1 1A17 17 0 0 1 3 4c0-.6.4-1 1-1h3.5c.6 0 1 .4 1 1 0 1.3.2 2.5.6 3.6.1.3 0 .7-.2 1z"/></svg>
      </span>
      <span class="contact-item__text">709-555-0147, 709-555-0192</span>
    </li>
    <li class="contact-item contact-item--web">
      <span class="contact-item__icon">
        <svg viewBox="0 0 24 24" fill="none" stroke="#050808" stroke-width="2"><circle cx="12" cy="12" r="9.5"/><ellipse cx="12" cy="12" rx="4" ry="9.5"/><line x1="2.5" y1="12" x2="21.5" y2="12"/></svg>
      </span>
      <span class="contact-item__text">www.norvanebuilders-example.com</span>
    </li>
    <li class="contact-item contact-item--address">
      <span class="contact-item__icon">
        <svg viewBox="0 0 24 24"><path fill="#050808" d="M12 2a6 6 0 0 0-6 6c0 4.5 6 10 6 10s6-5.5 6-10a6 6 0 0 0-6-6zm0 8.5a2.5 2.5 0 1 1 0-5 2.5 2.5 0 0 1 0 5z"/><path fill="none" stroke="#050808" stroke-width="2" d="M5 17l-2 5h18l-2-5"/></svg>
      </span>
      <span class="contact-item__text">42 Brenton Street Elk Harbour, NL B3K 7T2</span>
    </li>
  </ul>
  <svg class="safety-strip safety-strip--bottom" viewBox="0 0 850 60"><rect width="850" height="60" fill="url(#strip-light)"/></svg>
</section>
</body>
</html>
```